Need a Poster Design A3 for our Cricket Competition

We need a poster design for our upcoming T20 cricket competition Coastline Summer Cup (CSC).

it should say like this:

Bellwick Real Estate (logo supplied)
proudly presents

Coastline Summer Cup (logo supplied)

its a T20 cricket competition

starting 1st April 2018
Registrations Closing : 18th March

prizes worth $5000 to be won

for Registration contact: 0401937265 / 0402816394 and our Facebook page address..see last time's poster

and then sponsors
Updates

Hello.. We will be closing the contest earlier by 5 days so we need to get the design by Tuesday 13th Feb .. Thanks

Industry/Entity Type

Real Estate

Colors

Designer to choose colors to be used in the design.

Requirements
Must have
• emphasis on our main sponsor Bellwick Real Estate & our competition logo

```html
<!DOCTYPE html>
<html lang="en">
<head>
<meta charset="utf-8">
<title>Coastline Summer Cup – T20 Poster</title>
<link rel="stylesheet" href="https://fonts.googleapis.com/css2?family=Josefin+Sans:wght@600;700&family=Oswald:wght@400;500&display=swap">
<style>
  :root {
    --grass-light: #7fa64a;
    --grass-mid: #4f7a2c;
    --grass-dark: #22401a;
    --band: rgba(20, 40, 14, 0.72);
    --band-line: rgba(120, 150, 90, 0.35);
    --beige: #ddd3a0;
    --white: #ffffff;
    --navy: #1f2a6b;
    --ink: #2a2a2a;
  }
  * { margin: 0; padding: 0; box-sizing: border-box; }
  html, body { width: 914px; height: 1200px; overflow: hidden; background: #f2f2f0; }
  .poster {
    position: relative;
    width: 914px;
    height: 1200px;
    overflow: hidden;
    font-family: "Oswald", sans-serif;
    color: var(--white);
  }
  .poster__scene {
    position: absolute; inset: 0;
    background:
      linear-gradient(180deg, #5e8a36 0%, #3f6a24 22%, #2f5520 48%, #3c6526 66%, var(--grass-light) 82%, #6f9a3e 100%);
  }
  .poster__scene-shade {
    position: absolute; inset: 0;
    background: radial-gradient(ellipse at 50% 35%, rgba(255,255,255,0.08), rgba(0,0,0,0.25) 80%);
  }
  .sponsor-main {
    position: absolute; top: 96px; left: 0; width: 100%;
    text-align: center;
    font-family: "Josefin Sans", sans-serif; font-weight: 600;
    font-size: 40px; letter-spacing: 3px; text-transform: uppercase;
    color: var(--white);
  }
  .presents {
    position: absolute; top: 196px; left: 0; width: 100%;
    text-align: center;
    font-size: 46px; font-weight: 400; letter-spacing: 0;
    transform: scaleX(0.82);
  }
  .title {
    position: absolute; left: 146px; width: 620px;
    font-family: "Josefin Sans", sans-serif; font-weight: 700;
    text-align: center; line-height: 1; text-transform: uppercase;
  }
  .title--line1 { top: 292px; font-size: 96px; letter-spacing: 1px; }
  .title--line2 { top: 392px; font-size: 78px; letter-spacing: 1px; }
  .tagline {
    position: absolute; top: 462px; right: 148px;
    font-size: 30px; font-weight: 400;
    transform: scaleX(0.82); transform-origin: right center;
  }
  .comp-badge {
    position: absolute; left: 782px; top: 286px; width: 100px; height: 212px;
    background: var(--white);
    display: flex; align-items: center; justify-content: center;
  }
  .comp-badge__name {
    font-family: "Josefin Sans", sans-serif; font-weight: 700;
    font-size: 34px; color: var(--navy);
    writing-mode: vertical-rl;
    letter-spacing: 4px;
  }
  .band {
    position: absolute; left: 0; width: 100%;
    background: var(--band);
    border-top: 1px solid var(--band-line);
    display: flex; align-items: center;
  }
  .band--start { top: 586px; height: 71px; justify-content: center; }
  .band--close { top: 663px; height: 72px; justify-content: center; }
  .band--prize { top: 739px; height: 70px; justify-content: flex-end; padding-right: 31px; }
  .band__text {
    font-family: "Josefin Sans", sans-serif; font-weight: 600;
    color: var(--beige); text-transform: uppercase; padding-top: 6px;
  }
  .band--start .band__text { font-size: 42px; letter-spacing: 1px; }
  .band--close .band__text { font-size: 43px; letter-spacing: 1px; }
  .band__prize {
    font-size: 42px; font-weight: 500; color: var(--white);
    transform: scaleX(0.8); transform-origin: right center;
  }
  .contact {
    position: absolute; left: 218px; top: 972px;
    font-size: 30px; font-weight: 500; line-height: 44px;
    transform: scaleX(0.8); transform-origin: left top;
  }
  .sponsors {
    position: absolute; left: 218px; top: 1059px; width: 480px; height: 122px;
    background: var(--white); border-radius: 6px;
    display: grid; grid-template-columns: repeat(5, 1fr); grid-template-rows: 1fr 1fr;
    align-items: center; justify-items: center; padding: 6px 8px; gap: 4px;
  }
  .sponsors__name {
    font-family: "Oswald", sans-serif; font-weight: 500;
    font-size: 13px; line-height: 1.15; color: var(--ink);
    text-align: center; text-transform: uppercase;
  }
</style>
</head>
<body>
<main class="poster">
  <div class="poster__scene" role="img" aria-label="Photograph of a cricket field: a batsman's gloved hand resting on a bat at left, a red ball on the grass and stumps being knocked over at right, green trees blurred behind"></div>
  <div class="poster__scene-shade"></div>

  <div class="sponsor-main">Bellwick Real Estate</div>
  <p class="presents">proudly presents</p>

  <h1>
    <span class="title title--line1">Coastline</span>
    <span class="title title--line2">Summer Cup</span>
  </h1>
  <div class="comp-badge"><span class="comp-badge__name">CSC</span></div>
  <p class="tagline">its a T20 cricket competition</p>

  <div class="band band--start"><span class="band__text">Starting 1st April 2018</span></div>
  <div class="band band--close"><span class="band__text">Registrations Closing : 18th March</span></div>
  <div class="band band--prize"><span class="band__prize">prizes worth $5000 to be won</span></div>

  <p class="contact">for Registration contact:<br>0401937265 / 0402816394</p>

  <section class="sponsors" aria-label="Sponsors">
    <span class="sponsors__name">Honeycomb Sweets</span>
    <span class="sponsors__name">Ridgeway Freight</span>
    <span class="sponsors__name">Marlow Family Trust</span>
    <span class="sponsors__name">Kestrel</span>
    <span class="sponsors__name">Willowfield Cotton</span>
    <span class="sponsors__name">Bluegum Transport</span>
    <span class="sponsors__name">Orbit TV</span>
    <span class="sponsors__name">Greenleaf Grocers</span>
    <span class="sponsors__name">Northbay Services</span>
    <span class="sponsors__name">Parkline</span>
  </section>
</main>
</body>
</html>
```